Anesthesia Medical Practice Business Card

We need a business card to hand out to surgeons with my basic information. Something that stands out but is not over the top. The medical community is rather conservative. I'd like them to call me first when flipping through their rolodex of anesthesiologists. I'd like the card to communicate confidence, control, professionalism yet serenity. I don't want the card to be pricey to print.

he logo will be provided as a vector graphic in addition to a complete business card design including the logo

Ravi Pell Okonedo, M.D.
Board Certified Anesthesiologist

(310) 555-0186

rokonedo@mailvane.net

Mailing Address:
48315 Corbel Ave.
Suite 270-4863
Los Angeles, CA 90024

A logo that inegrates my initials perhaps
RO MD
My initials are RO and MD as in Medical Doctor

or
perhaps a physician in surgical mask and cap caring for a patient

Target Market(s)

Surgeons who need anesthesia services

Industry/Entity Type

Medical

Requirements
Must have
• the logo will be provided as a vector graphic in addition to a complete business card design including the logo

Ravi Pell Okonedo, M.D.

(310) 555-0186

rokonedo@mailvane.net

Mailing Address:
48315 Corbel Ave.
Suite 270-4863
Los Angeles, CA 90024

Nice to have
• A logo that inegrates my initials perhaps
RO MD

or

```html
<!DOCTYPE html>
<html lang="en">
<head>
<meta charset="utf-8">
<title>Ravi Pell Okonedo, M.D. — Business Card</title>
<link href="https://fonts.googleapis.com/css2?family=Questrial&display=swap" rel="stylesheet">
<style>
  :root {
    --ink: #33393c;
    --sky: #8cc4f0;
    --card: #ffffff;
    --backdrop: #e6e7e8;
  }
  * { margin: 0; padding: 0; box-sizing: border-box; }
  html, body {
    width: 1200px;
    height: 1000px;
    overflow: hidden;
    background: var(--backdrop);
    font-family: "Questrial", "Century Gothic", sans-serif;
    color: var(--ink);
  }
  .sheet {
    width: 1200px;
    height: 1000px;
    display: flex;
    flex-direction: column;
    align-items: center;
    justify-content: center;
    gap: 50px;
  }
  .card {
    position: relative;
    width: 840px;
    height: 420px;
    background: var(--card);
    border-radius: 40px;
    box-shadow: 0 2px 10px rgba(0, 0, 0, 0.12);
  }

  /* Front */
  .card-front {
    display: flex;
    flex-direction: column;
    align-items: center;
    justify-content: center;
  }
  .wordmark-large {
    font-size: 150px;
    line-height: 1;
    letter-spacing: 4px;
    color: var(--ink);
  }
  .specialty {
    margin-top: 14px;
    font-size: 52px;
    line-height: 1;
    color: var(--ink);
  }

  /* Back */
  .card-back { padding: 46px 60px; }
  .identity { position: absolute; left: 60px; top: 48px; }
  .doctor-name {
    font-size: 34px;
    color: var(--sky);
    line-height: 1.1;
  }
  .doctor-title {
    font-size: 25px;
    color: var(--ink);
    margin-top: 4px;
  }
  .wordmark-small {
    position: absolute;
    right: 80px;
    top: 82px;
    font-size: 58px;
    line-height: 1;
    letter-spacing: 2px;
    color: var(--ink);
  }
  .mailing {
    position: absolute;
    left: 60px;
    bottom: 52px;
    font-size: 26px;
    line-height: 1.28;
  }
  .mailing-label { color: var(--sky); }
  .contact {
    position: absolute;
    right: 70px;
    bottom: 52px;
    font-size: 26px;
    list-style: none;
  }
  .contact-item {
    display: flex;
    align-items: center;
    gap: 16px;
    margin-top: 24px;
  }
  .contact-icon { width: 22px; height: 22px; flex: none; }
</style>
</head>
<body>
  <main class="sheet">
    <section class="card card-front" aria-label="Card front">
      <div class="wordmark-large">RO MD</div>
      <div class="specialty">Anesthesiologist</div>
    </section>

    <section class="card card-back" aria-label="Card back">
      <div class="identity">
        <div class="doctor-name">Ravi Pell Okonedo, M.D.</div>
        <div class="doctor-title">Board Certified Anesthesiologist</div>
      </div>
      <div class="wordmark-small">RO MD</div>

      <address class="mailing" style="font-style: normal;">
        <div class="mailing-label">Mailing Address:</div>
        <div>48315 Corbel Ave.</div>
        <div>Suite 270-4863</div>
        <div>Los Angeles, CA 90024</div>
      </address>

      <ul class="contact">
        <li class="contact-item">
          <svg class="contact-icon" viewBox="0 0 22 22" aria-hidden="true">
            <rect x="6" y="1.5" width="10" height="19" rx="2" fill="none" stroke="var(--sky)" stroke-width="1.6"/>
            <line x1="9.5" y1="17.5" x2="12.5" y2="17.5" stroke="var(--sky)" stroke-width="1.4"/>
          </svg>
          <span>(310) 555-0186</span>
        </li>
        <li class="contact-item">
          <svg class="contact-icon" viewBox="0 0 22 22" aria-hidden="true">
            <rect x="1.5" y="5" width="19" height="12" fill="none" stroke="var(--sky)" stroke-width="1.6"/>
            <polyline points="1.5,5 11,12 20.5,5" fill="none" stroke="var(--sky)" stroke-width="1.4"/>
          </svg>
          <span>rokonedo@mailvane.net</span>
        </li>
      </ul>
    </section>
  </main>
</body>
</html>
```